"End of year wishes" - Electronic card

Quenlax is a regulatory consulting company in the cosmetic sector. We provide premium services and have 12 years of experience.
Please visit our website for more information: https://quenlax.example
Like every year, we would like to send an electronic design to our clients and partners to wish them happy holidays. This year, we would like to share two good news with them: offer them a surprise (to be revealed later on) and invite them to visit our new brand new website. We relay on your talent and imagination for the design! We need something very professional, serious, beautiful and in line with our graphic layout (see our company website)

Target Market(s)

cosmetic brands

Industry/Entity Type

Cosmetics

Requirements
Must have
• The following statement should be included to the design:

We wish you a Happy Holiday and a Marvelous New Year 2021!
As December is the month of giving, we have a surprise for you. Please contact your dedicated Account Manager to find out more!

Good news never comes alone, we've also updated our website in order to serve you better. We hope you like it as much as we do.
Please enjoy the experience: www.quenlax.example

```html
<!DOCTYPE html>
<html lang="en">
<head>
<meta charset="utf-8">
<title>Quenlax – End of Year Wishes</title>
<link rel="stylesheet" href="https://fonts.googleapis.com/css2?family=Yellowtail&family=Poppins:wght@400;600&display=swap">
<style>
  :root {
    --ink: #231f20;
    --accent: #86c906;
    --accent-soft: #e7f3cf;
    --paper: #ffffff;
    --foliage-dark: #7d7f7c;
    --foliage-light: #f1f6e8;
  }
  * { margin: 0; padding: 0; box-sizing: border-box; }
  html, body { width: 1200px; height: 1117px; overflow: hidden; background: var(--paper); }
  .card {
    position: relative;
    width: 1200px;
    height: 1117px;
    background: var(--paper);
    color: var(--ink);
    font-family: "Poppins", sans-serif;
  }
  .greeting {
    position: absolute;
    top: 126px;
    left: 0;
    width: 100%;
    text-align: center;
    font-family: "Yellowtail", cursive;
    font-size: 64px;
    line-height: 86px;
    color: var(--ink);
    font-weight: 400;
  }
  .divider {
    position: absolute;
    top: 346px;
    left: 542px;
    display: flex;
    gap: 29px;
  }
  .divider span { width: 17px; height: 17px; background: var(--accent); display: block; }
  .message {
    position: absolute;
    left: 0;
    width: 100%;
    text-align: center;
    font-size: 21.5px;
    line-height: 47px;
  }
  .message-surprise { top: 437px; }
  .message-website { top: 578px; }
  .message-link { top: 720px; font-weight: 600; }
  .highlight { color: var(--accent); font-weight: 600; }
  .decor { position: absolute; inset: 0; width: 1200px; height: 1117px; pointer-events: none; }
  .foliage {
    position: absolute;
    left: 0;
    bottom: 0;
    width: 1200px;
    height: 240px;
    background: linear-gradient(180deg, rgba(255,255,255,0) 0%, var(--foliage-light) 35%, #b9bcb6 75%, var(--foliage-dark) 100%);
  }
</style>
</head>
<body>
  <main class="card">
    <h1 class="greeting">We wish you a Happy Holiday and<br>a Marvelous New Year 2021!</h1>

    <div class="divider" aria-hidden="true"><span></span><span></span><span></span></div>

    <p class="message message-surprise">As December is the month of giving, <span class="highlight">we have a surprise for you.</span><br>Please contact your dedicated Account Manager to find out more!</p>

    <p class="message message-website">Good news never comes alone, we've also updated our website<br>in order to serve you better. We hope you like it as much as we do.</p>

    <p class="message message-link">Please enjoy the experience: <a class="highlight" href="https://quenlax.example" style="text-decoration:none">www.quenlax.example</a></p>

    <div class="foliage" role="img" aria-label="Illustrated border of snowy pine branches along the bottom edge"></div>

    <svg class="decor" viewBox="0 0 1200 1117" aria-hidden="true">
      <g fill="var(--accent)">
        <circle cx="87" cy="383" r="4.5"/>
        <circle cx="52" cy="543" r="3.5"/>
        <circle cx="43" cy="678" r="1.5"/>
        <circle cx="177" cy="747" r="5"/>
        <circle cx="1163" cy="508" r="3.5"/>
        <circle cx="1023" cy="697" r="3"/>
        <circle cx="1153" cy="829" r="6" opacity="0.8"/>
        <circle cx="575" cy="899" r="5"/>
        <circle cx="769" cy="892" r="3.5"/>
        <circle cx="235" cy="946" r="5"/>
        <circle cx="334" cy="922" r="3"/>
        <circle cx="742" cy="951" r="4"/>
      </g>
    </svg>
    <svg class="decor" viewBox="0 0 1200 1117">
      <g fill="var(--accent-soft)">
        <circle role="img" aria-label="Snowflake ornament" cx="83" cy="463" r="15"/>
        <circle role="img" aria-label="Snowflake ornament" cx="104" cy="635" r="32"/>
        <circle role="img" aria-label="Snowflake ornament" cx="83" cy="851" r="48"/>
        <circle role="img" aria-label="Snowflake ornament" cx="264" cy="835" r="27"/>
        <circle role="img" aria-label="Snowflake ornament" cx="1140" cy="423" r="16"/>
        <circle role="img" aria-label="Snowflake ornament" cx="1099" cy="566" r="30"/>
        <circle role="img" aria-label="Snowflake ornament" cx="1119" cy="709" r="34"/>
        <circle role="img" aria-label="Snowflake ornament" cx="873" cy="865" r="16"/>
        <circle role="img" aria-label="Snowflake ornament" cx="1045" cy="890" r="54"/>
      </g>
    </svg>
  </main>
</body>
</html>
```